Sales Process Flyer

Attached is a sketch (2 pages) Id like to have a 1 page "flyer" that will explain the sales strategy for a new recruit.
Ill need to edit this down the road, so if you do it in Illustrator we will be able to handle that.
If you plenvo sales funnel you will see what im going for with the bad funnel drawing.
Id like to have icons with the text thats on the 2nd page (although it would all be 1 page)
Our brand guidelines are attached with some example pieces we have done in the past
Would like this to have an infographic type look

Something I didnt work in the sketch is below.
Estimated Sales Time:
25% - Meeting & Managing Existing Clients
25% - Free Assessments & Proposals
25% - Cold Calling
25% - New Customer Meetings & Networking

Plenvo

```html
<!DOCTYPE html>
<html lang="en">
<head>
<meta charset="utf-8">
<title>Sales Strategy</title>
<link rel="stylesheet" href="https://fonts.googleapis.com/css2?family=Ubuntu:wght@500;700&display=swap">
<style>
  :root {
    --backdrop: #dcdcdc;
    --charcoal: #4a494b;
    --brand-blue: #156ea0;
    --mid-grey: #9b9a9b;
    --white: #ffffff;
  }
  * { box-sizing: border-box; margin: 0; padding: 0; }
  html, body {
    width: 1200px; height: 900px; overflow: hidden;
    background: var(--backdrop);
    font-family: "Ubuntu", sans-serif;
  }
  .flyer {
    position: absolute; left: 276px; top: 30px;
    width: 527px; height: 683px;
    transform: scale(1.23); transform-origin: top left;
    background: var(--white);
    box-shadow: 0 2px 8px rgba(0,0,0,.25);
  }
  .top-band { position: absolute; left: 0; top: 0; width: 100%; height: 26px; background: var(--charcoal); }
  .title-band {
    position: absolute; left: 0; top: 26px; width: 100%; height: 49px;
    background: var(--brand-blue); color: var(--white);
    display: flex; align-items: center; justify-content: center;
    font-size: 29px; font-weight: 700; letter-spacing: .3px;
  }
  .pillar-band { position: absolute; left: 0; top: 75px; width: 100%; height: 81px; background: var(--mid-grey); }
  .pillar {
    position: absolute; top: 13px; width: 118px; height: 54px; border-radius: 27px;
    display: flex; align-items: center; justify-content: center;
    color: var(--white); font-size: 18px; font-weight: 500;
  }
  .pillar--blue { background: var(--brand-blue); z-index: 2; }
  .pillar--dark { background: var(--charcoal); z-index: 1; }
  .bottom-band { position: absolute; left: 0; bottom: 0; width: 100%; height: 21px; background: var(--charcoal); }

  .step-note {
    position: absolute; left: 0; width: 190px;
    background: var(--charcoal); color: var(--white);
    display: flex; align-items: center; justify-content: center; text-align: center;
    font-size: 10.5px; font-weight: 500; line-height: 1.3;
  }
  .lost-reasons {
    position: absolute; left: 0; top: 568px; width: 190px; height: 94px;
    background: var(--mid-grey); color: var(--white);
    padding: 16px 0 0 32px; font-size: 17px; font-weight: 500; line-height: 1.27;
  }

  .funnel-ribbons { position: absolute; left: 0; top: 0; width: 527px; height: 683px; }
  .stage {
    position: absolute; background: var(--brand-blue); color: var(--white);
    border: 1px solid #0f5a84;
    display: flex; flex-direction: column; align-items: center; justify-content: center;
    text-align: center; font-size: 12px; font-weight: 500; line-height: 1.3;
  }
</style>
</head>
<body>
<main class="flyer">
  <div class="top-band"></div>
  <h1 class="title-band">Sales Strategy</h1>
  <nav class="pillar-band">
    <span class="pillar pillar--blue" style="left:88px">Strategy</span>
    <span class="pillar pillar--dark" style="left:205px">Effort</span>
    <span class="pillar pillar--blue" style="left:323px">Sell</span>
  </nav>

  <div class="step-note" style="top:184px;height:55px">- ... Page Created on Website<br>- Specific E-mail Created<br>- 500 E-mails Sent</div>
  <div class="step-note" style="top:253px;height:72px">- Phone call follow up with c....<br>- Phone call follow up with opens<br>- Phone call follow up with ...<br>make free assessment pitch</div>
  <div class="step-note" style="top:340px;height:55px">Run free asscent</div>
  <div class="step-note" style="top:416px;height:56px">Meeting Scheduled</div>
  <div class="step-note" style="top:492px;height:56px">Proposal</div>
  <div class="lost-reasons">Lost - Price<br>Lost - Timeline<br>Lost - Unknown</div>

  <svg class="funnel-ribbons" viewBox="0 0 527 683" aria-hidden="true">
    <g fill="var(--charcoal)">
      <polygon points="212,230 287,230 482,272 397,272"/>
      <polygon points="247,308 307,308 447,350 377,350"/>
      <polygon points="272,385 332,385 417,425 357,425"/>
      <polygon points="292,462 347,462 402,502 347,502"/>
      <polygon points="307,539 357,539 387,578 337,578"/>
    </g>
  </svg>

  <div class="stage" style="left:197px;top:188px;width:323px;height:48px;border-radius:24px">5% - e-mail sent</div>
  <div class="stage" style="left:229px;top:265px;width:260px;height:48px;border-radius:24px">10% - First Contact<span>180 goal</span></div>
  <div class="stage" style="left:255px;top:343px;width:208px;height:47px;border-radius:24px">25% - Assessmant<span>60 goal</span></div>
  <div class="stage" style="left:280px;top:420px;width:157px;height:47px;border-radius:24px">50% - Meeting<span>32 goal</span></div>
  <div class="stage" style="left:302px;top:497px;width:114px;height:47px;border-radius:24px">75% - Proposal<span>16 goal</span></div>
  <div class="stage" style="left:320px;top:573px;width:78px;height:46px;border-radius:23px">won</div>

  <div class="bottom-band"></div>
</main>
</body>
</html>
```